business card double side design

We need a business card design for our company PLUMlearnhub. DOUBLE SIDED. We provide continuing education programs & courses across North America. Our website is www.plumlearnhub.example - please use the grey pinstrip concept as part of the design. Compliment the branding that is occuring on that site!
Please use pantones daa520 and 3f3151. Verdana for text. I have attached our logo.
I would like the logo & website address www.PLUMlearnhub.example on the front of the card, all other info on the backside. The final design should communicate authority and credibility.

• verdanda

• pantones daa520 and 3f3151. Verdana for text.
• must compliment the branding occuring on the www.PLUMlearnhub.example

```html
<!DOCTYPE html>
<html lang="en">
<head>
<meta charset="utf-8">
<title>PLUMlearnhub business card</title>
<link href="https://fonts.googleapis.com/css2?family=Source+Sans+3:wght@400;600;700&display=swap" rel="stylesheet">
<style>
  :root {
    --gold: #daa520;
    --plum: #3f3151;
    --card: #f5f5f5;
    --ink: #222222;
    --backdrop: #cbcbcb;
  }
  * { margin: 0; padding: 0; box-sizing: border-box; }
  html, body { width: 1200px; height: 1005px; overflow: hidden; }
  body {
    background: var(--backdrop);
    font-family: "Source Sans 3", Verdana, sans-serif;
    color: var(--ink);
    position: relative;
  }
  .card {
    position: absolute;
    left: 220px;
    width: 760px;
    height: 434px;
    background: var(--card);
    overflow: hidden;
    box-shadow: 0 6px 14px rgba(0,0,0,0.18);
  }
  .card--front { top: 48px; }
  .card--back { top: 522px; }
  .card svg.bands { position: absolute; left: 0; top: 0; width: 760px; height: 434px; }

  .brand {
    position: absolute;
    display: flex;
    align-items: center;
    gap: 18px;
  }
  .brand__dot {
    border-radius: 50%;
    background: var(--gold);
    flex: none;
  }
  .brand__name {
    font-weight: 700;
    color: var(--plum);
    letter-spacing: 0.5px;
  }
  .card--front .brand { left: 50%; top: 100px; transform: translateX(-50%); }
  .card--front .brand__dot { width: 130px; height: 130px; }
  .card--front .brand__name { font-size: 54px; }

  .front-web {
    position: absolute;
    left: 0; right: 0;
    top: 298px;
    height: 28px;
    line-height: 28px;
    text-align: center;
    font-size: 20px;
    color: var(--ink);
  }

  .card--back .brand { right: 70px; top: 70px; gap: 14px; }
  .card--back .brand__dot { width: 100px; height: 100px; }
  .card--back .brand__name { font-size: 40px; }

  .person { position: absolute; left: 70px; top: 130px; }
  .person__name { font-size: 32px; font-weight: 600; color: var(--plum); line-height: 1.1; }
  .person__role { font-size: 17px; color: var(--ink); margin-top: 2px; }

  .contact { position: absolute; left: 385px; top: 212px; font-size: 18px; line-height: 27px; }
  .contact__row { display: flex; align-items: center; gap: 12px; }
  .contact__row svg { width: 16px; height: 16px; flex: none; }
  .contact__addr { margin-top: 4px; }

  .social { position: absolute; left: 110px; top: 320px; font-size: 17px; }
  .social__icons { display: flex; gap: 6px; margin-top: 8px; }
  .social__icons span { width: 26px; height: 26px; background: var(--plum); border-radius: 3px; }

  .back-web {
    position: absolute;
    left: 415px;
    top: 388px;
    font-size: 19px;
    color: #ffffff;
  }
</style>
</head>
<body>

<section class="card card--front" aria-label="Card front">
  <svg class="bands" viewBox="0 0 760 434" aria-hidden="true">
    <polygon points="0,398 760,338 760,342 0,402" fill="var(--gold)"/>
    <polygon points="0,406 760,346 760,434 0,434" fill="var(--plum)"/>
    <polygon points="175,318 250,310 250,314" fill="var(--plum)"/>
    <polygon points="510,310 585,302 510,314" fill="var(--plum)"/>
  </svg>
  <div class="brand">
    <span class="brand__dot"></span>
    <span class="brand__name">PLUMlearnhub</span>
  </div>
  <p class="front-web">www.PLUMlearnhub.example</p>
</section>

<section class="card card--back" aria-label="Card back">
  <svg class="bands" viewBox="0 0 760 434" aria-hidden="true">
    <polygon points="0,400 400,390 400,434 0,434" fill="var(--gold)"/>
    <polygon points="400,360 760,330 760,434 380,434" fill="var(--plum)"/>
  </svg>

  <div class="person">
    <h1 class="person__name">Dana Whitfield</h1>
    <p class="person__role">Technical Support</p>
  </div>

  <div class="brand">
    <span class="brand__dot"></span>
    <span class="brand__name">PLUMlearnhub</span>
  </div>

  <div class="contact">
    <p class="contact__row">
      <svg viewBox="0 0 16 16" aria-hidden="true"><path d="M3 2h3l1 4-2 1a9 9 0 0 0 4 4l1-2 4 1v3a1 1 0 0 1-1 1A13 13 0 0 1 2 3a1 1 0 0 1 1-1z" fill="var(--gold)"/></svg>
      555.014.2287
    </p>
    <p class="contact__row">
      <svg viewBox="0 0 16 16" aria-hidden="true"><rect x="1" y="3" width="14" height="10" fill="var(--gold)"/><path d="M1 3l7 6 7-6" fill="none" stroke="#ffffff" stroke-width="1.2"/></svg>
      dana@PLUMlearnhub.example
    </p>
    <p class="contact__addr">Suite 140, 58 Larkspur Lane<br>Maple Ridge, Ontario</p>
  </div>

  <div class="social">
    <p>Follow us on</p>
    <div class="social__icons" aria-label="Social profiles">
      <span></span><span></span><span></span>
    </div>
  </div>

  <p class="back-web">www.PLUMlearnhub.example</p>
</section>

</body>
</html>
```